" A empresa tem como principal atrativo a grande variedade de joias infantis. Nosso maior diferencial são as peças de alta joalheria para crianças e a confecção de joias exclusivas e personalizadas para o publico de todas as idades. Temos um atelier para atendimento com hora marcada e o e-commerce é nossa principal vitrine. É possível conhecer algumas peças e parte da identidade da marca no nosso site www.brilhomirim.com.br e no instagram @brilhomirim "

```html
<!DOCTYPE html>
<html lang="pt-BR">
<head>
<meta charset="utf-8">
<title>Brilho Mirim — Envelope</title>
<link rel="stylesheet" href="https://fonts.googleapis.com/css2?family=Cormorant+Garamond:wght@500;600&display=swap">
<style>
  :root {
    --backdrop: #efece7;
    --envelope-grey: #9a9a9a;
    --band-white: #ffffff;
    --brand-blue: #8fcbdc;
    --text-white: #ffffff;
  }
  html, body {
    margin: 0;
    padding: 0;
    width: 1200px;
    height: 1200px;
    overflow: hidden;
    background: var(--backdrop);
  }
  .envelope {
    display: block;
    width: 1200px;
    height: 1200px;
  }
  .envelope__body { fill: var(--envelope-grey); }
  .envelope__band { fill: var(--band-white); }
  .envelope__band-edge { fill: var(--brand-blue); }
  .brand-name {
    font-family: "Cormorant Garamond", serif;
    font-weight: 600;
    font-size: 11px;
    letter-spacing: 0.6px;
    fill: var(--brand-blue);
  }
  .brand-dot { fill: var(--brand-blue); }
  .contact-line {
    font-family: "Cormorant Garamond", serif;
    font-weight: 500;
    font-size: 4.6px;
    fill: var(--text-white);
  }
</style>
</head>
<body>
<svg class="envelope" viewBox="0 0 500 500" xmlns="http://www.w3.org/2000/svg" aria-label="Envelope Brilho Mirim, planificado">
  <!-- envelope die-cut -->
  <g class="envelope__shape">
    <polygon class="envelope__body" points="108,122 250,93 394,122 394,386 250,328 106,386"/>
    <polygon class="envelope__body" points="108,150 88,155 88,255 108,262"/>
    <polygon class="envelope__body" points="394,150 410,156 410,254 394,262"/>
  </g>

  <!-- front band -->
  <g class="envelope__band-group">
    <rect class="envelope__band-edge" x="88" y="156" width="322" height="96"/>
    <rect class="envelope__band" x="88" y="160" width="322" height="88"/>
  </g>

  <!-- brand name -->
  <g class="brand">
    <circle class="brand-dot" cx="122" cy="190" r="4"/>
    <text class="brand-name" x="130" y="194">BRILHO MIRIM</text>
  </g>

  <!-- contact block on back flap (set upside down for folding) -->
  <g class="contact" transform="rotate(180 172 306)">
    <text class="contact-line" x="214" y="298" text-anchor="end">www.brilhomirim.com.br  |  @brilhomirim</text>
    <text class="contact-line" x="214" y="306" text-anchor="end">11 0000 0000  |  0000 000 000</text>
    <text class="contact-line" x="214" y="314" text-anchor="end">Rua Aurora, 120</text>
  </g>
</svg>
</body>
</html>
```